Text Box for making an update on our website

We need an awesome "Text Box" so that our Users can make an amazing Post or update on our website or App.

Let's make something super duper like Pictavo, Chatterly, Quibb or Posteo text box but a bit more amazing....

I've included our current desktop and Mobile "Text Box" which needs love :)

Our Text Box by default makes a Post "Private" the User can change it to "Public"

I have included what a final "Post" looks like on our site.

Could we incorporate a bit of the "Post" design into the "Create Post" design..... maybe make the header similar.

thanks

Morgan

Target Market(s)

Health Care, Hospitals, Caregivers, Nurses

Industry/Entity Type

Health Care

Font styles to use
Other font styles liked:
• Comfortaa

Requirements
Must have
• Our main colors are

#1D44B8 - Blue
#D85097 - Pink
Nice to have
• Super clean and simple. Happy and Easy to use
Should not have
• Complicated

Too many colors

```html
<!DOCTYPE html>
<html lang="en">
<head>
<meta charset="UTF-8">
<title>Create Post</title>
<link href="https://fonts.googleapis.com/css2?family=Poppins:wght@400;500&display=swap" rel="stylesheet">
<style>
  :root {
    --brand-blue: #2850B9;
    --icon-blue: #2A4DB5;
    --brand-pink: #D85097;
    --page-bg: #F4F4F4;
    --card-bg: #FFFFFF;
    --field-border: #DCDCDC;
    --divider: #E6E6E6;
    --placeholder: #C9C9C9;
    --white: #FFFFFF;
  }
  * { box-sizing: border-box; margin: 0; padding: 0; }
  html, body {
    width: 1200px;
    height: 406px;
    overflow: hidden;
    background: var(--page-bg);
    font-family: "Poppins", sans-serif;
  }
  .post-composer {
    position: absolute;
    left: 121px;
    top: 41px;
    width: 957px;
    height: 323px;
    background: var(--card-bg);
    box-shadow: 0 2px 6px rgba(0,0,0,0.18);
  }
  .composer-header {
    position: relative;
    height: 78px;
    background: var(--brand-blue);
    color: var(--white);
  }
  .composer-title {
    position: absolute;
    left: 44px;
    top: 18px;
    font-size: 29px;
    font-weight: 400;
    letter-spacing: 0.2px;
  }
  .close-button {
    position: absolute;
    right: 22px;
    top: 10px;
    width: 22px;
    height: 22px;
  }
  .privacy-select {
    position: absolute;
    right: 10px;
    top: 43px;
    display: flex;
    align-items: center;
    gap: 8px;
    font-size: 19px;
  }
  .privacy-select svg { width: 13px; height: 13px; }
  .post-field {
    position: absolute;
    left: 26px;
    top: 97px;
    width: 912px;
    height: 131px;
    border: 1px solid var(--field-border);
  }
  .post-placeholder {
    position: absolute;
    left: 10px;
    top: 8px;
    font-size: 21px;
    color: var(--placeholder);
  }
  .resize-handle {
    position: absolute;
    right: 6px;
    bottom: 5px;
    width: 20px;
    height: 20px;
  }
  .composer-toolbar {
    position: absolute;
    left: 0;
    top: 246px;
    width: 957px;
    height: 77px;
    border-top: 1px solid var(--divider);
  }
  .tool {
    position: absolute;
    top: 18px;
    width: 40px;
    height: 40px;
    display: flex;
    align-items: center;
    justify-content: center;
  }
  .tool svg {
    width: 38px;
    height: 38px;
    fill: none;
    stroke: var(--icon-blue);
    stroke-width: 1.6;
    stroke-linecap: round;
    stroke-linejoin: round;
  }
  .tool-photos { left: 96px; }
  .tool-location { left: 233px; }
  .tool-tag { left: 371px; }
  .tool-emoji { left: 516px; }
  .tool-attach { left: 659px; }
  .send-button {
    position: absolute;
    right: 0;
    top: -1px;
    width: 156px;
    height: 78px;
    background: var(--brand-pink);
    display: flex;
    align-items: center;
    justify-content: center;
  }
  .send-button svg {
    width: 36px;
    height: 36px;
    fill: none;
    stroke: var(--white);
    stroke-width: 1.8;
    stroke-linejoin: round;
    stroke-linecap: round;
  }
</style>
</head>
<body>
  <section class="post-composer">
    <header class="composer-header">
      <h1 class="composer-title">Create Post</h1>
      <svg class="close-button" viewBox="0 0 22 22" aria-label="Close">
        <path d="M2 2 L20 20 M20 2 L2 20" stroke="#FFFFFF" stroke-width="2" stroke-linecap="round"/>
      </svg>
      <div class="privacy-select">
        <svg viewBox="0 0 13 13"><path d="M2 4 L6.5 9 L11 4" fill="none" stroke="#FFFFFF" stroke-width="1.6" stroke-linecap="round" stroke-linejoin="round"/></svg>
        <span>Private</span>
      </div>
    </header>

    <div class="post-field">
      <span class="post-placeholder">Share a New Post</span>
      <svg class="resize-handle" viewBox="0 0 20 20" aria-hidden="true">
        <path d="M3 3 L17 17 M3 3 L3 9 M3 3 L9 3 M17 17 L17 11 M17 17 L11 17" fill="none" stroke="#BDBDBD" stroke-width="1.4" stroke-linecap="round"/>
      </svg>
    </div>

    <nav class="composer-toolbar">
      <div class="tool tool-photos" aria-label="Add photos">
        <svg viewBox="0 0 38 38">
          <rect x="4" y="13" width="22" height="20"/>
          <path d="M10 13 V7 H32 V27 H26"/>
          <path d="M15 7 V3 H36 V22 H32" stroke-dasharray="2 2.5"/>
          <path d="M4 29 L11 22 L16 27 L20 23 L26 29"/>
          <circle cx="19" cy="18" r="2"/>
        </svg>
      </div>
      <div class="tool tool-location" aria-label="Add location">
        <svg viewBox="0 0 38 38">
          <path d="M19 35 C12 26 8 20 8 14 A11 11 0 0 1 30 14 C30 20 26 26 19 35 Z"/>
          <circle cx="19" cy="14" r="3.5"/>
        </svg>
      </div>
      <div class="tool tool-tag" aria-label="Add tag">
        <svg viewBox="0 0 38 38">
          <path d="M20 5 H33 V18 L17 34 L4 21 Z"/>
          <circle cx="27" cy="11" r="2"/>
        </svg>
      </div>
      <div class="tool tool-emoji" aria-label="Add emoji">
        <svg viewBox="0 0 38 38">
          <circle cx="19" cy="19" r="14"/>
          <circle cx="14" cy="15" r="1" fill="#2A4DB5"/>
          <circle cx="24" cy="15" r="1" fill="#2A4DB5"/>
          <path d="M12 22 Q19 29 26 22"/>
        </svg>
      </div>
      <div class="tool tool-attach" aria-label="Attach file">
        <svg viewBox="0 0 38 38">
          <path d="M30 17 L17 30 A7 7 0 0 1 7 20 L21 6 A4.5 4.5 0 0 1 27.5 12.5 L14.5 25.5 A2 2 0 0 1 11.5 22.5 L23 11"/>
        </svg>
      </div>
      <div class="send-button" aria-label="Send post">
        <svg viewBox="0 0 36 36">
          <path d="M33 3 L3 15 L15 20 L20 33 Z"/>
          <path d="M33 3 L15 20"/>
        </svg>
      </div>
    </nav>
  </section>
</body>
</html>
```